Bonusheft für Patienten als kleine DIN A6 Broschüre
Zielgruppe
Bonusheft für Patienten als kleine DIN A6 Broschüre in der Zahn-Prophylaxe. Die Texte haben wir bereits vollständig formuliert, auch die Gliederung ist vorgegeben.
Wir sind eine Zahnarztpraxis mit dem Schwerpunkt Prophylaxe. Für unsere Prophylaxeabteilung möchten wir eine DIN A6 Broschüre entwerfen lassen, die als Bonusheft für Patienten dient.
Inhalt: Informationen über unsere Praxis, die leitende Mitarbeiterin, individuelle Risiken und Empfehlungen der Patienten. Auch Fakten und Tipps zur Verbesserung der Mundhygiene und Putzgewohnheiten werden Beschrieben.
Aufgabenstellung
Broschüre als DIN A6 Bonusheft mit circa sieben gestalteten Seiten, bei denen wir den Aufbau und die exakten Texte bereits vollständig vorgeben. Zusätzlich folgen mehrere gleiche Seiten, bei denen die Termine und Stempel eingetragen werden (ca. fünf Seiten).
Für Ihre Orientierung haben wir unsere Fotos und Farbschema von vorhandenen Designs unserer Praxis bereitgestellt.
Orientieren Sie sich gerne an unserer vorhandenen Homepage im Hinblick auf unseren Stil und das Praxislogo.
Homepage: www.zahnpraxis-am-lindenhof.de
Wir stellen einige Fotos zur Verwendung bereit. Falls nötig, verwenden Sie auch Stock Fotos.
Im folgenden werden wir den gewünschten Aufbau mit den Texten je Seite detailliert vorstellen. Ihre Aufgabe ist es, dies in ein modernes, frisches, ansprechendes und kompetentes Design umzusetzen.
1. Seite / Cover
- Mit Praxislogo
- Text: „Mein Prophylaxepass“
2. Seite:
- Überschrift: „Sie lassen nicht jeden an Ihre Zähne? Wir auch nicht.“
-Text: „Herzlich Willkommen! Mein Name ist Merle und ich arbeite als leitende Mitarbeiterin im Lindenhof Zentrum Halmsbrück. Momentan befinde ich mich in der Weiterbildung zur Dentalhygienikerin und bin begeistert von der Arbeit in der präventiven Zahnmedizin. Mit meinem Wissen und meiner Erfahrung möchte ich dazu beitragen, dass unsere Patienten sich bei uns wohl und gut betreut fühlen. Ich freue mich darauf, Ihnen zu helfen, Ihre Zahngesundheit zu erhalten und zu verbessern!“
- Foto einer Mitarbeiterin
4. Seite:
- Überschrift: „Die professionelle Zahnreinigung – Wellness & Prävention“
- Text: „Eine wichtige Präventionsmaßnahme ist die regelmäßige Zahnreinigung in unserem Prophylaxe-Zentrum. Karies, Mundgeruch und Zahnfleischerkrankungen werden effektiv vorgebeugt. Die Zahnreinigung ist ein Teil der individuell geplanten Prophylaxe und eine sinnvolle Ergänzung der häus..

```html
<!DOCTYPE html>
<html lang="de">
<head>
<meta charset="utf-8">
<title>Mein Prophylaxepass – Broschüre</title>
<link href="https://fonts.googleapis.com/css2?family=Questrial&family=Montserrat:wght@700&family=Arimo:wght@700&display=swap" rel="stylesheet">
<style>
:root{
  --stage:#000;
  --page:#ececec;
  --white:#fff;
  --beige:#cbc5a5;
  --beige-dark:#b4ad8f;
  --ink:#1f1f1f;
  --label:#fff;
}
*{box-sizing:border-box;margin:0;padding:0}
html,body{width:1200px;height:969px;overflow:hidden;background:var(--stage)}
body{position:relative;font-family:"Questrial",sans-serif;color:var(--ink)}
.page{position:absolute;width:287px;height:405px;background:var(--page);overflow:hidden}
.page::before{content:"";position:absolute;left:0;top:0;right:0;height:15px;background:var(--beige);border-bottom:2px solid var(--beige-dark)}
.page::after{content:"";position:absolute;left:0;bottom:0;right:0;height:17px;background:var(--beige);border-top:2px solid var(--beige-dark)}
.page--cover{background:var(--white)}
.page--cover::before,.page--cover::after{display:none}
.label{position:absolute;width:287px;text-align:center;color:var(--label);font-family:"Arimo",sans-serif;font-weight:700;font-size:21px}
.heading{position:absolute;left:8px;font-family:"Montserrat",sans-serif;font-weight:700;font-size:14.5px;line-height:18px;letter-spacing:-.2px;white-space:nowrap}
.copy{position:absolute;left:9px;font-size:10.6px;line-height:12.7px;white-space:nowrap}
.photo{position:absolute}
/* Cover */
.cover-rule{position:absolute;height:2px;background:var(--beige)}
.brand{position:absolute;left:0;width:287px;text-align:center;font-size:30px;line-height:34px;color:var(--ink)}
.cover-title{position:absolute;left:0;width:287px;text-align:center;font-size:22px}
/* Lists */
.checklist{position:absolute;list-style:none;font-size:13.6px;white-space:nowrap}
.checklist li{height:20.2px;display:flex;align-items:center;gap:11px}
.box{width:13px;height:13px;border:1.5px solid var(--ink);background:var(--white);flex:none}
/* Forms */
.row{position:absolute;left:8px;font-size:10px;white-space:nowrap;display:flex;align-items:center;gap:8px}
.row--indent{left:16px}
.opt{display:inline-flex;align-items:center;gap:2px}
.opt::before{content:"";width:8px;height:8px;border:1.3px solid var(--ink);border-radius:50%}
.blank{display:inline-block;width:82px;border-bottom:1px solid var(--ink);margin-left:2px}
.divider{position:absolute;left:8px;right:8px;height:2px;background:var(--ink)}
.form-heading{position:absolute;left:8px;font-family:"Montserrat",sans-serif;font-weight:700;font-size:13px;letter-spacing:-.3px}
</style>
</head>
<body>

<!-- Seite 1 -->
<section class="page page--cover" style="left:13px;top:11px">
  <div class="cover-rule" style="left:9px;top:80px;width:69px"></div>
  <div class="cover-rule" style="left:209px;top:80px;width:69px"></div>
  <div class="brand" style="top:98px">Zahnpraxis<br>am Lindenhof</div>
  <div class="cover-rule" style="left:9px;top:186px;width:269px"></div>
  <div class="cover-title" style="top:192px">Mein Prophylaxepass</div>
  <div class="photo" role="img" aria-label="Foto des Praxisgebäudes aus rotem Backstein unter blauem Himmel" style="left:0;top:230px;width:287px;height:175px;background:linear-gradient(180deg,#7fb3e0 0%,#cfe3f2 35%,#8a5a44 60%,#6b4736 85%,#7e8c5a 100%)"></div>
</section>
<div class="label" style="left:13px;top:424px">Seite 1 / Cover</div>

<!-- Seite 2 -->
<section class="page" style="left:311px;top:11px">
  <h2 class="heading" style="top:29px;font-size:14px">Sie lassen nicht jeden an Ihre Zähne?</h2>
  <div class="photo" role="img" aria-label="Porträtfoto eines lächelnden Patienten" style="left:9px;top:53px;width:109px;height:126px;background:linear-gradient(160deg,#e6e8ea,#b8a08c 55%,#2d3440)"></div>
  <div class="photo" role="img" aria-label="Foto einer Mitarbeiterin mit Zahnmodell" style="left:118px;top:53px;width:161px;height:160px;background:linear-gradient(160deg,#7a7a7a,#d9c2b0 45%,#5f7d6c 80%)"></div>
  <div class="heading" style="top:188px;font-size:14px">Wir auch nicht.</div>
  <p class="copy" style="top:214px;font-size:10.6px;line-height:15.3px">Herzlich Willkommen!<br>Mein Name ist Merle und ich arbeite als leitende<br>Mitarbeiterin im Lindenhof Zentrum Halmsbrück.<br>Momentan befinde ich mich in der Weiterbildung<br>zur Dentalhygienikerin und bin begeistert von der<br>Arbeit in der präventiven Zahnmedizin.<br>Mit meinem Wissen und meiner Erfahrung möchte<br>ich dazu beitragen, dass unsere Patienten sich bei<br>uns wohl und gut betreut fühlen.<br>Ich freue mich darauf, Ihnen zu helfen,<br>Ihre Zahngesundheit zu erhalten und zu verbessern!</p>
</section>
<div class="label" style="left:311px;top:424px">Seite 2</div>

<!-- Seite 3 -->
<section class="page" style="left:607px;top:11px">
  <h2 class="heading" style="top:17px">Die professionelle Zahnreinigung<br>Wellness &amp; Prävention</h2>
  <p class="copy" style="top:58px">Eine wichtige Präventionsmaßnahme ist die<br>regelmäßige Zahnreinigung in unserem<br>Prophylaxe-Zentrum.<br>Karies, Mundgeruch und Zahnfleischerkrankungen<br>werden effektiv vorgebeugt. Die Zahnreinigung ist<br>ein Teil der individuell geplanten Prophylaxe und<br>eine sinnvolle Ergänzung der häuslichen Zahnpflege,<br>gerade an den Stellen, wo die eigene Zahnbürste<br>nicht hinkommt. Schonend werden alle harten und<br>weichen Beläge von allen Zahnoberflächen entfernt<br>inklusive Kaffee-, Tee- und Raucherbelägen.</p>
  <div class="photo" role="img" aria-label="Foto einer Zahnreinigung im Behandlungsstuhl" style="left:43px;top:203px;width:108px;height:109px;background:linear-gradient(150deg,#dfe4ea,#c9a68f 55%,#f0e4dc)"></div>
  <div class="photo" role="img" aria-label="Foto einer lächelnden Patientin im Behandlungsstuhl" style="left:151px;top:203px;width:93px;height:109px;background:linear-gradient(160deg,#bcd9ef,#d6b77f 45%,#2f4b6a)"></div>
  <p class="copy" style="top:318px">Natürlich weiße Zähne ! Nach der professionellen<br>Zahnreinigung stellt sich Ihre natürliche Zahnfarbe<br>wieder ein und ein frisches Mundgefühl entsteht.<br>In den meisten Fällen werden die Zähne nach der<br>Prophylaxe heller. Erhöhen Sie Ihre Lebensqualität!</p>
</section>
<div class="label" style="left:607px;top:424px">Seite 3</div>

<!-- Seite 4 -->
<section class="page" style="left:902px;top:11px">
  <h2 class="heading" style="top:19px">Moderne Technik für eine<br>bessere Behandlung</h2>
  <p class="copy" style="top:62px">Für unsere Prophylaxebehandlungen nutzen wir<br>aktuelle Behandlungsmethoden und bedienen uns<br>neuer Technologie wie dem Aquaflux Prophylaxe-<br>System.<br>Dadurch gewährleisten wir für unsere Patienten eine<br>leise und angenehme Behandlung. Gleichzeitig<br>stellen wir eine ausgezeichnete Behandlungsqualität<br>sicher, welche Ihre Zähne nachhaltig schützt und<br>Krankheiten vorbeugt.</p>
  <div class="photo" role="img" aria-label="Foto einer lächelnden Patientin mit Zahnfarbskala" style="left:7px;top:193px;width:270px;height:190px;background:linear-gradient(150deg,#bfe0f5,#e0c08a 40%,#2e5576 80%,#dfe8ef)"></div>
</section>
<div class="label" style="left:902px;top:424px">Seite 4</div>

<!-- Seite 5 -->
<section class="page" style="left:14px;top:507px">
  <h2 class="heading" style="top:19px;font-size:14px">Risikoanalyse</h2>
  <ul class="checklist" style="left:51px;top:64px">
    <li><span class="box"></span>Karisaktivität</li>
    <li><span class="box"></span>Empfindliches Zahnfleisch</li>
    <li><span class="box"></span>Erosionen / Säureschäden</li>
    <li><span class="box"></span>Zahnschmelzverlust</li>
    <li><span class="box"></span>Weicher Zahnschmelz</li>
    <li><span class="box"></span>Halitosis (Mundgeruch)</li>
    <li><span class="box"></span>Zahnverfärbungen</li>
    <li><span class="box"></span>Rauchen</li>
    <li><span class="box"></span>Retainer</li>
  </ul>
</section>
<div class="label" style="left:14px;top:919px">Seite 5</div>

<!-- Seite 6 -->
<section class="page" style="left:311px;top:507px">
  <h2 class="heading" style="top:19px;font-size:14px">Ergänzende Pflegetipps</h2>
  <ul class="checklist" style="left:14px;top:64px;font-size:13.2px">
    <li><span class="box"></span>1. Zahnseide</li>
    <li><span class="box"></span>2. Superfloss</li>
    <li><span class="box"></span>3. Zahnseidesticks</li>
    <li><span class="box"></span>4. Interdentalbürstchen</li>
    <li><span class="box"></span>5. Zungenreinigung</li>
    <li><span class="box"></span>6. Intensiv Fluoridierung</li>
    <li><span class="box"></span>7. 1x wöchentliche Spezial Zahnpasta</li>
    <li><span class="box"></span>8. Munddusche</li>
    <li><span class="box"></span>9. Mundspüllösung</li>
  </ul>
</section>
<div class="label" style="left:311px;top:919px">Seite 6</div>

<!-- Seite 7 -->
<section class="page" style="left:608px;top:507px">
  <div class="row" style="top:26px">Prophylaxe Pass überreicht am: <span class="blank" style="width:65px"></span></div>
  <div class="row" style="top:44px">Ihr Intervall:</div>
  <div class="row" style="top:62px"><span class="opt">3 Monate</span><span class="opt">4 Monate</span><span class="opt">6 Monate</span><span class="opt">12 Monate</span></div>
  <div class="row" style="top:83px">Heutiger Termin:</div>
  <div class="row" style="top:104px">Intervall:</div>
  <div class="row row--indent" style="top:118px"><span class="opt">3 Monate</span><span class="opt">4 Monate</span><span class="opt">6 Monate</span><span class="opt">12 Monate</span></div>
  <div class="row" style="top:132px">Terminart:</div>
  <div class="row row--indent" style="top:146px;gap:22px"><span class="opt">Regulärer Termin</span><span class="opt">Kompakttermin</span></div>
  <div class="row" style="top:173px">Datum | Uhrzeit: <span class="blank"></span></div>
  <div class="row" style="top:193px">Behandelt von: <span class="blank"></span></div>
  <div class="divider" style="top:216px"></div>
  <div class="form-heading" style="top:229px">Ihr nächster Termin:</div>
  <div class="row" style="top:253px">Ihr Intervall:</div>
  <div class="row" style="top:270px"><span class="opt">3 Monate</span><span class="opt">4 Monate</span><span class="opt">6 Monate</span><span class="opt">12 Monate</span></div>
  <div class="row" style="top:297px">Terminart:</div>
  <div class="row row--indent" style="top:312px;gap:22px"><span class="opt">Regulärer Termin</span><span class="opt">Kompakttermin</span></div>
  <div class="row" style="top:338px">Datum | Uhrzeit: <span class="blank"></span></div>
  <div class="row" style="top:358px">Behandelt von: <span class="blank"></span></div>
</section>
<div class="label" style="left:608px;top:919px">Seite 7</div>

<!-- Seite 8-12 -->
<section class="page" style="left:901px;top:507px">
  <div class="form-heading" style="top:19px">Weitere Termine:</div>
  <div class="row" style="top:36px">Intervall:</div>
  <div class="row" style="top:54px"><span class="opt">3 Monate</span><span class="opt">4 Monate</span><span class="opt">6 Monate</span><span class="opt">12 Monate</span></div>
  <div class="row" style="top:68px">Terminart:</div>
  <div class="row row--indent" style="top:83px;gap:22px"><span class="opt">Regulärer Termin</span><span class="opt">Kompakttermin</span></div>
  <div class="row" style="top:104px">Datum | Uhrzeit: <span class="blank"></span></div>
  <div class="row" style="top:125px">Behandelt von: <span class="blank"></span></div>
  <div class="divider" style="top:143px"></div>
  <div class="row" style="top:153px">Intervall:</div>
  <div class="row" style="top:170px"><span class="opt">3 Monate</span><span class="opt">4 Monate</span><span class="opt">6 Monate</span><span class="opt">12 Monate</span></div>
  <div class="row" style="top:186px">Terminart:</div>
  <div class="row row--indent" style="top:200px;gap:22px"><span class="opt">Regulärer Termin</span><span class="opt">Kompakttermin</span></div>
  <div class="row" style="top:220px">Datum | Uhrzeit: <span class="blank"></span></div>
  <div class="row" style="top:241px">Behandelt von: <span class="blank"></span></div>
  <div class="divider" style="top:265px"></div>
  <div class="row" style="top:274px">Intervall:</div>
  <div class="row" style="top:292px"><span class="opt">3 Monate</span><span class="opt">4 Monate</span><span class="opt">6 Monate</span><span class="opt">12 Monate</span></div>
  <div class="row" style="top:307px">Terminart:</div>
  <div class="row row--indent" style="top:321px;gap:22px"><span class="opt">Regulärer Termin</span><span class="opt">Kompakttermin</span></div>
  <div class="row" style="top:342px">Datum | Uhrzeit: <span class="blank"></span></div>
  <div class="row" style="top:362px">Behandelt von: <span class="blank"></span></div>
</section>
<div class="label" style="left:901px;top:919px">Seite 8-12</div>

</body>
</html>
```